Advertising flyer for proofreading business.

Hello everyone,

I need an advertising flyer for a new proofreading company in Australia.

I would like your design in be in two sizes:
- A4 (to be posted on noticeboards),
- A6 (to be printed in larger quantity to give away)
(please see the size specification file attached).

The text file is attached (Ad Text) and it contains lots of information. Please feel free to include your choice of text from the text file, but please include Poster title, and highlight 'ESL' and students discounts.

I understand that it is impossible to include the same amount of information on A6 and A4, so please feel free to chose what fits on each of them, but please keep the design similar.

I have attached our company logo, but feel free to adjust it to the poster design (feel free to change the color as well). The original logo file contains circle around it, please feel free to remove it and include only the typeset as it can be seen here: http://www.vellumcheck.com.au/.

Flyers will be printed, so please see the specification file for details.

I will do my best to respond to feedback as soon as possible.

I appreciate your participation, time and help,
Best wishes,
Radoslaw

Target Market(s)

Students, authors

Industry/Entity Type

Business

Colors

Designer to choose colors to be used in the design.

Requirements
Must have
• It would be good if poster is easy to spot on busy noticeboards and attract attention.
• Please keep the poster in the positive/optimistic mood, and so that it focuses on students, maybe photos of graduates(?).
• Poster title,
• Please include the list of proof-read documents as they are described in the attached text file (Ad Text).
• Please highlight students discounts and ESL.
Nice to have
• I would like to leave the creative freedom to all designers so at this point I have not adjusted the Look and Feel sliders. Please feel free to offer your own take on this.
• It would be nice if most of the text could be fit to the poster.

```html
<!DOCTYPE html>
<html lang="en">
<head>
<meta charset="utf-8">
<title>Vellumcheck – Professional Proofreading Services</title>
<link rel="stylesheet" href="https://fonts.googleapis.com/css2?family=Montserrat:wght@400;500;600;700&display=swap">
<style>
  :root {
    --page-bg: #ececec;
    --ink: #000000;
    --paper: #ffffff;
    --texture-dark: #0a0a0a;
    --texture-mid: #2a2a2a;
    --body-text: #111111;
  }
  * { box-sizing: border-box; margin: 0; padding: 0; }
  html, body {
    width: 1200px; height: 1200px; overflow: hidden;
    background: var(--page-bg);
    font-family: "Montserrat", Arial, sans-serif;
  }
  .flyer {
    position: absolute; left: 254px; top: 111px;
    width: 693px; height: 981px;
    background: var(--ink);
    color: var(--paper);
    box-shadow: 0 2px 6px rgba(0,0,0,0.12);
    overflow: hidden;
  }
  .hero {
    position: relative; height: 481px;
  }
  .hero-texture {
    position: absolute; inset: 0;
    background:
      radial-gradient(ellipse 46% 40% at 50% 50%, var(--texture-dark) 0%, rgba(10,10,10,0.6) 60%, transparent 100%),
      linear-gradient(180deg, var(--texture-mid) 0%, #1a1a1a 55%, #3a3a3a 85%, var(--ink) 100%);
  }
  .hero-title {
    position: absolute; top: 72px; left: 0; right: 0;
    text-align: center; font-weight: 700;
    font-size: 29px; line-height: 33px; letter-spacing: 0.3px;
  }
  .brand-name {
    position: absolute; top: 250px; left: 0; right: 0;
    text-align: center; font-weight: 500;
    font-size: 72px; line-height: 80px; color: var(--paper);
  }
  .intro {
    height: 149px; padding: 17px 26px 0;
  }
  .intro h2 {
    font-size: 20px; font-weight: 600; margin-bottom: 8px; letter-spacing: 0.2px;
  }
  .intro ul { list-style: none; font-size: 14.5px; line-height: 16.5px; }
  .intro li { padding-left: 11px; text-indent: -11px; margin-bottom: 7px; }
  .details {
    background: var(--paper); color: var(--body-text);
    height: 272px; padding: 15px 26px 0;
  }
  .details h3 { font-size: 15.5px; font-weight: 700; line-height: 19px; }
  .details ul { list-style: none; font-size: 12.8px; line-height: 16.8px; }
  .details li { padding-left: 10px; text-indent: -10px; }
  .doc-types { margin-bottom: 10px; }
  .price-guide li { margin-bottom: 2px; }
  .price-guide strong { font-weight: 700; }
  .contact {
    height: 79px; text-align: center; padding-top: 16px;
  }
  .contact-cta { font-size: 11px; font-weight: 500; letter-spacing: 0.6px; }
  .contact-list {
    display: flex; justify-content: center; gap: 18px;
    margin-top: 9px; font-size: 11px; font-weight: 500; letter-spacing: 0.3px;
  }
  .contact-item { display: flex; align-items: center; gap: 6px; }
  .contact-item svg { width: 14px; height: 14px; }
</style>
</head>
<body>
<article class="flyer">
  <section class="hero">
    <div class="hero-texture" role="img" aria-label="Dark background of faint overlapping serif and script text lines"></div>
    <h1 class="hero-title">PROFESSIONAL<br>PROOFREADING<br>SERVICES</h1>
    <div class="brand-name">Vellumcheck</div>
  </section>

  <section class="intro">
    <h2>Professional, English-language proofreading</h2>
    <ul>
      <li>• Help with English as a second language (ESL - native English speaker with English Honours degree will correct all English language errors, spelling and grammar mistakes.</li>
      <li>• Includes referencing and editing for style, coherence and clarity.</li>
      <li>• Fast, negotiable time-frames.</li>
    </ul>
  </section>

  <section class="details">
    <h3>Types of proof-read documents:</h3>
    <ul class="doc-types">
      <li>• essays / assignments / theses / resumes</li>
      <li>• business correspondence / training manuals / newsletters</li>
      <li>• advertising copy / brochures / catalogues / media releases</li>
      <li>• websites / presentations / speeches</li>
      <li>• novels / short stories</li>
    </ul>
    <h3>Price guide:</h3>
    <ul class="price-guide">
      <li>• Prices starting at <strong>$20 per page</strong>. Additional charges may apply for longer and/or more complex documents (e.g. documents requiring specialist help with English as a second language).</li>
      <li>• Discounts for not-for-profit organisations and students. Special student discount rate: <strong>$25 per hour</strong> - roughly 1000 words (4 pages) of well-written text.</li>
      <li>• Package deals on documents over 50,000 words.</li>
      <li>• Fast turnaround times (same day service can be provided by special arrangement).</li>
    </ul>
  </section>

  <footer class="contact">
    <p class="contact-cta">CONTACT US FOR AN OBLIGATION-FREE QUOTE</p>
    <div class="contact-list">
      <span class="contact-item">
        <svg viewBox="0 0 14 14" aria-hidden="true"><circle cx="7" cy="7" r="7" fill="#fff"/><path d="M4.6 3.6l1.3-.3.8 1.9-.9.7c.5 1 1.2 1.7 2.2 2.2l.7-.9 1.9.8-.3 1.3c-3.2 0-5.7-2.5-5.7-5.7z" fill="#000"/></svg>
        0400 555 123
      </span>
      <span class="contact-item">
        <svg viewBox="0 0 14 14" aria-hidden="true"><circle cx="7" cy="7" r="7" fill="#fff"/><rect x="3.6" y="4.6" width="6.8" height="4.8" fill="#000"/><path d="M3.8 4.8L7 7.3l3.2-2.5" stroke="#fff" stroke-width="0.8" fill="none"/></svg>
        proofing@vellumcheck.com.au
      </span>
      <span class="contact-item">www.vellumcheck.com.au</span>
    </div>
  </footer>
</article>
</body>
</html>
```